Turning Lecture Halls into Studios of Bold Discovery

This is for a book cover aimed at professors in higher education who want to infuse creative thinking into their classroom. It should have the title on the cover (see name of project). Our first idea is to have a stack of academic type books on a desk in black and white and then have a colorful rainbow light thread hitting the books. However, we are open to options! It has to be sophisticated, cool, and creative ;)

Target Market(s)

Higher Education Instructors

Industry/Entity Type

education

Font styles to use
Serif
Sans Serif

Requirements
Nice to have
• a creative feel of some sort
Should not have
• lightbulbs

```html
<!DOCTYPE html>
<html lang="en">
<head>
<meta charset="utf-8">
<title>Turning Lecture Halls into Studios of Bold Discovery — Cover</title>
<link rel="stylesheet" href="https://fonts.googleapis.com/css2?family=Barlow+Condensed:wght@600;700&display=swap">
<style>
  :root {
    --backdrop: #d9d9d9;
    --paper: #f2f2f0;
    --title-blue: #4a72b8;
    --title-pink: #e8659f;
    --ink-yellow: #f6c232;
    --ink-orange: #f28a3c;
    --ink-pink: #ea4f8c;
    --ink-purple: #8a5bb8;
    --ink-blue: #3f86d0;
    --ink-green: #3fb28a;
  }
  html, body {
    margin: 0;
    padding: 0;
    width: 1200px;
    height: 1200px;
    overflow: hidden;
    background: var(--backdrop);
  }
  .cover {
    position: absolute;
    left: 167px;
    top: 0;
    width: 866px;
    height: 1200px;
    background: var(--paper);
    font-family: "Barlow Condensed", "Arial Narrow", sans-serif;
  }
  .cover-title {
    position: absolute;
    left: 71px;
    top: 22px;
    width: 724px;
    height: 460px;
    overflow: visible;
  }
  .title-line {
    font-family: "Barlow Condensed", "Arial Narrow", sans-serif;
    font-weight: 600;
    fill: var(--title-blue);
  }
  .title-key {
    font-family: "Barlow Condensed", "Arial Narrow", sans-serif;
    font-weight: 700;
    fill: var(--title-pink);
  }
  .cover-art {
    position: absolute;
    left: 71px;
    top: 600px;
    width: 747px;
    height: 450px;
    border-radius: 48% 52% 40% 60% / 55% 45% 55% 45%;
    background:
      radial-gradient(ellipse at 85% 25%, rgba(246,194,50,0.85), rgba(242,138,60,0) 45%),
      linear-gradient(160deg,
        var(--ink-yellow) 0%,
        var(--ink-orange) 22%,
        var(--ink-pink) 40%,
        var(--ink-purple) 58%,
        var(--ink-blue) 76%,
        var(--ink-green) 100%);
    opacity: 0.55;
    filter: blur(6px);
  }
  .cover-author {
    position: absolute;
    left: 0;
    right: 0;
    top: 1100px;
    margin: 0;
    text-align: center;
    font-weight: 600;
    font-size: 42px;
    letter-spacing: 3px;
    color: var(--title-blue);
    line-height: 1;
  }
</style>
</head>
<body>
  <main class="cover">
    <svg class="cover-title" viewBox="0 0 724 460" role="heading" aria-level="1" aria-label="Turning Lecture Halls into Studios of Bold Discovery">
      <text class="title-line" x="0" y="78" font-size="104" textLength="724" lengthAdjust="spacingAndGlyphs">TURNING LECTURE HALLS</text>
      <text class="title-line" x="0" y="172" font-size="104" textLength="724" lengthAdjust="spacingAndGlyphs">INTO STUDIOS OF BOLD</text>
      <text class="title-key" x="0" y="446" font-size="340" textLength="724" lengthAdjust="spacingAndGlyphs">DISCOVERY</text>
    </svg>
    <div class="cover-art" role="img" aria-label="Watercolour illustration of rainbow ink streams rising from an open book"></div>
    <p class="cover-author">AUTHOR NAME</p>
  </main>
</body>
</html>
```